WWW.TRESSALO.IT BUSINNES CARD

WE NEED A BUSINESS CARD . I HAVE A COMPANY IN ITALY NR 1 IN HAIR MEDICAL CARE AN HAIR REPLECEMENT . IN CARD I NEED WRITE WEB ADDRESS, MAIL , ADDRESS, TELEPHONE NUMBER , AND NAME
IN THE BACK SIDE I NEED MY DOCTOR LOGO .
MY WEB SITE IS WWW.TRESSALO.IT
Updates

Hai bisogno di giorni extra per la revisione

Target Market(s)

CONSUMER B2C

Industry/Entity Type

Hair And Beauty

Contact Information for Business Card

I WANT A MEDICAL BUSINESS CARD.

Font styles to use
Other font styles liked:
• VERDANA

Colors
33a6d7
3176b5
85abd2
aedbee
eaf1f7
ffffff

Requirements
Must have
• I NEED MY LOGO AND LOGO OF DR TRESSALO

```html
<!DOCTYPE html>
<html lang="it">
<head>
<meta charset="utf-8">
<title>Tressalo – Business Card</title>
<link rel="stylesheet" href="https://fonts.googleapis.com/css2?family=Open+Sans:wght@400;600;800&display=swap">
<style>
  :root{
    --stage:#4a4a4a;
    --sky:#2db0e2;
    --brand-blue:#33a6d7;
    --deep-blue:#1f5aa6;
    --mid-blue:#3176b5;
    --soft-blue:#85abd2;
    --pale-blue:#aedbee;
    --ink:#4a4a4a;
    --white:#ffffff;
  }
  *{margin:0;padding:0;box-sizing:border-box}
  html,body{width:1200px;height:912px;overflow:hidden}
  body{
    background:var(--stage);
    font-family:"Open Sans",Verdana,sans-serif;
    display:flex;flex-direction:column;align-items:center;justify-content:center;gap:56px;
  }
  .card{width:640px;height:366px;position:relative;overflow:hidden;box-shadow:0 10px 24px rgba(0,0,0,.35)}
  .card-back{background:var(--sky)}
  .mascot-area{
    position:absolute;left:255px;top:50px;width:130px;height:270px;border-radius:65px 65px 60px 60px;
    background:linear-gradient(180deg,#7a4a2a 0%,#8a5a36 55%,#f2b995 100%);
  }
  .card-front{background:var(--white)}
  .card-front svg.waves{position:absolute;inset:0}
  .brand{position:absolute;right:52px;top:34px;text-align:left;z-index:1}
  .brand-row{display:flex;align-items:center;gap:10px}
  .brand-dot{width:34px;height:34px;border-radius:50%;background:var(--brand-blue)}
  .brand-name{font-weight:800;font-size:40px;color:var(--mid-blue);letter-spacing:.5px;line-height:1}
  .brand-tagline{font-size:10px;font-weight:600;color:var(--mid-blue);letter-spacing:.3px;margin-top:6px;margin-left:44px}
  .person{position:absolute;left:52px;top:176px;z-index:1}
  .person-name{font-size:27px;font-weight:800;color:var(--deep-blue);line-height:1.1}
  .person-name .surname{color:var(--brand-blue)}
  .person-role{font-size:15px;color:var(--ink);margin-top:4px}
  .contacts{position:absolute;left:52px;top:248px;list-style:none;z-index:1}
  .contacts li{display:flex;align-items:center;gap:12px;font-size:15px;color:var(--ink);height:22px}
  .contacts svg{width:14px;height:14px;flex:none}
  .address{
    position:absolute;right:18px;top:196px;color:var(--white);font-size:15px;
    transform:rotate(-24deg);transform-origin:right center;white-space:nowrap;
  }
</style>
</head>
<body>

<section class="card card-back" aria-label="Retro del biglietto">
  <div class="mascot-area" role="img" aria-label="Mascotte dr. Tressalo: capello in camice da medico"></div>
</section>

<section class="card card-front" aria-label="Fronte del biglietto">
  <svg class="waves" viewBox="0 0 640 366" aria-hidden="true">
    <path d="M250 250 L560 140" stroke="var(--pale-blue)" stroke-width="1.2" fill="none"/>
    <path d="M320 150 Q560 140 625 95" stroke="var(--brand-blue)" stroke-width="2" fill="none"/>
    <path d="M640 150 C560 175 470 230 400 290 C360 325 320 350 280 366 L640 366 Z" fill="var(--brand-blue)"/>
    <path d="M0 340 C160 336 300 316 420 246" stroke="var(--mid-blue)" stroke-width="6" fill="none"/>
    <path d="M0 352 C170 348 310 330 430 258" stroke="var(--deep-blue)" stroke-width="4" fill="none"/>
    <path d="M0 362 C180 358 320 344 440 270" stroke="var(--mid-blue)" stroke-width="3" fill="none"/>
    <path d="M40 368 C190 366 330 356 450 282" stroke="var(--soft-blue)" stroke-width="2" fill="none"/>
  </svg>

  <div class="brand">
    <div class="brand-row">
      <span class="brand-dot"></span>
      <span class="brand-name">Tressalo</span>
    </div>
    <div class="brand-tagline">CURA E REINTEGRAZIONE DEI CAPELLI</div>
  </div>

  <div class="person">
    <div class="person-name">Luca <span class="surname">Ferretti</span></div>
    <div class="person-role">Founder &amp; CEO</div>
  </div>

  <ul class="contacts">
    <li><svg viewBox="0 0 16 16"><path d="M4 1l3 3-2 2c1 2 3 4 5 5l2-2 3 3-2 3C7 15 1 9 1 3z" fill="var(--deep-blue)"/></svg>+390458812604</li>
    <li><svg viewBox="0 0 16 16"><rect x="1" y="3" width="14" height="10" fill="var(--deep-blue)"/><path d="M1 3l7 6 7-6" stroke="#fff" fill="none"/></svg>info@tressalo.it</li>
    <li><svg viewBox="0 0 16 16"><circle cx="8" cy="8" r="7" fill="var(--mid-blue)"/><path d="M1 8h14M8 1c-3 4-3 10 0 14M8 1c3 4 3 10 0 14" stroke="#fff" fill="none" stroke-width=".8"/></svg>www.tressalo.it</li>
  </ul>

  <div class="address">Via dei Tigli 14 Verona Italy</div>
</section>

</body>
</html>
```